Roofing Company needs YOU to help put us on top!

Brindlecrest Roofing, a fresh new company with quality and Innovation in mind, needs your help to stand out in the competitive Chicago market. With over 30 years of experience, all the right people and tools for the job, the only thing we are missing is your creative ideas in web design to help us grow our online presence.
Our Company offers exceptional quality at reasonable prices, we work for the everyday people both blue collar and white collar.

We have used MakerHarbor in the past with multiple successful campaigns, we are excited to see what you can come up with for our website.

www.BrindlecrestRoofing-demo.net will be the domain

We will be hiring a photographer for visual content on our pages later. Stock photos are okay to use but should follow theme.

Thank you for taking the time on the submissions, if you have any questions don't hesitate to ask and we will provide whatever is needed to you.

Target Market(s)

Homeowners & Commercial Clients between 21-65

Industry/Entity Type

Roofing

Coding

Coded - Design and coding required

Number of Pages Required

4 page

Font styles to use
Sans Serif

Colors
ffffff
ec1f27
000000
5c5c5c
757575
b2b2b2

Requirements
Must have
• Color Scheme - should follow around our logo
• As for pages we were looking for an About, Services, Projects (gallery page) and Contact.
• Main page please include social media links and a a place so people could use coinwell to make payments
• Website should work on desktop as well as mobile platforms
Nice to have
• A Live chat feature would be nice if possible
Should not have
• Obscure Colors or Common web templates

```html
<!DOCTYPE html>
<html lang="en">
<head>
<meta charset="utf-8">
<title>Brindlecrest Roofing</title>
<link rel="stylesheet" href="https://fonts.googleapis.com/css2?family=Montserrat:wght@300;400;500;600;700&family=Open+Sans:ital,wght@0,400;0,600;0,700;1,400&display=swap">
<style>
:root{
  --white:#ffffff;
  --red:#ec1f27;
  --red-dark:#c4151c;
  --black:#000000;
  --ink:#111111;
  --night:#1b1b1b;
  --grey-dark:#5c5c5c;
  --grey:#757575;
  --grey-light:#b2b2b2;
  --line:#e4e4e4;
  --text:#333333;
  --chat:#5cb531;
}
*{margin:0;padding:0;box-sizing:border-box}
html,body{width:1200px;height:4918px;overflow:hidden}
body{position:relative;background:var(--white);font-family:"Open Sans",Arial,sans-serif;color:var(--text)}
.abs{position:absolute}
.head{font-family:"Montserrat",Arial,sans-serif}

/* header */
.site-header{left:0;top:0;width:1200px;height:88px;background:var(--ink)}
.brand{left:180px;top:22px;display:flex;align-items:center;gap:10px}
.brand-mark{width:40px;height:40px;background:var(--red)}
.brand-name{font-family:"Montserrat",sans-serif;font-weight:700;font-size:17px;color:var(--white);line-height:1.1;width:130px}
.main-nav{left:420px;top:34px;display:flex;gap:26px}
.main-nav a{font-family:"Montserrat",sans-serif;font-size:13px;font-weight:600;color:var(--white);text-decoration:none;letter-spacing:.3px}
.header-phone{left:920px;top:18px;width:100px;text-align:center;color:var(--white);font-size:12px}
.header-phone svg{display:block;margin:0 auto 6px}
.search-btn{left:1026px;top:0;width:66px;height:88px;background:var(--red);display:flex;align-items:center;justify-content:center}

/* hero */
.hero{left:0;top:88px;width:1200px;height:627px;background:linear-gradient(160deg,#5a4a3e 0%,#3c342f 35%,#2a2624 70%,#1d1b1a 100%)}
.hero-shade{left:0;top:88px;width:1200px;height:627px;background:rgba(0,0,0,.35)}
.hero-title{left:0;top:318px;width:1200px;text-align:center;font-family:"Montserrat",sans-serif;font-weight:300;font-size:52px;line-height:64px;color:var(--white)}
.hero-title strong{font-weight:700}
.slide-arrow{top:393px;width:52px;height:52px;background:rgba(0,0,0,.55);display:flex;align-items:center;justify-content:center}
.social-rail{left:1158px;top:292px;width:34px;display:flex;flex-direction:column;gap:2px}
.social-rail span{width:34px;height:30px;background:var(--white);display:flex;align-items:center;justify-content:center}
.social-rail span i{width:10px;height:10px;border-radius:50%;background:var(--ink);display:block}
.quote-card{left:760px;top:613px;width:266px;height:142px;background:var(--black);z-index:2}
.quote-card p{padding:22px 20px 0;font-family:"Montserrat",sans-serif;font-size:13px;font-weight:500;line-height:18px;color:var(--white);text-transform:uppercase}
.quote-card a{position:absolute;left:0;bottom:0;width:266px;height:42px;background:var(--red);color:var(--white);font-family:"Montserrat",sans-serif;font-size:13px;font-weight:600;text-decoration:none;display:flex;align-items:center;justify-content:center}

/* stats */
.stats{left:0;top:715px;width:1200px;height:177px;background:#1c1c1c}
.stat-number{left:272px;top:785px;font-family:"Montserrat",sans-serif;font-size:40px;font-weight:700;color:var(--white)}
.stat-title{left:466px;top:766px;font-family:"Montserrat",sans-serif;font-size:22px;font-weight:500;color:var(--white)}
.stat-sub{left:466px;top:800px;width:380px;font-size:13px;font-style:italic;line-height:19px;color:var(--grey-light)}

/* about */
.about-photo{left:148px;top:951px;width:377px;height:508px;background:linear-gradient(180deg,#f3f3f3 0%,#e9d9a8 25%,#c9a45a 55%,#6d5a3d 100%)}
.about-title{left:606px;top:970px;width:520px;font-family:"Montserrat",sans-serif;font-size:30px;font-weight:400;line-height:40px;color:#222}
.about-list{left:606px;top:1132px;width:500px;list-style:none}
.about-list li{position:relative;padding-left:18px;font-size:12.5px;line-height:17px;color:var(--grey);margin-bottom:10px}
.about-list li:before{content:"";position:absolute;left:0;top:5px;width:7px;height:7px;background:var(--red)}
.read-more{left:632px;top:1380px;font-family:"Montserrat",sans-serif;font-size:13px;font-weight:700;color:#222;text-decoration:none;border-bottom:2px solid var(--red);padding-bottom:4px}

/* feature band */
.feature{top:1469px;width:400px;height:253px;padding:50px 30px 0 118px;color:var(--white)}
.feature svg{position:absolute;left:22px;top:52px}
.feature h3{font-family:"Montserrat",sans-serif;font-size:28px;font-weight:400;line-height:34px}
.feature p{margin-top:12px;font-size:12.5px;line-height:17px;color:rgba(255,255,255,.8)}

/* services */
.section-title{left:0;width:1200px;text-align:center;font-family:"Montserrat",sans-serif;font-weight:400;color:#222}
.services-intro{left:300px;top:1845px;width:600px;text-align:center;font-size:13px;line-height:19px;color:var(--grey)}
.services-grid{left:164px;top:1895px;width:870px;height:597px;display:grid;grid-template-columns:repeat(3,290px);grid-template-rows:318px 279px}
.service{text-align:center;padding-top:50px;border-right:1px solid var(--line);border-bottom:1px solid var(--line)}
.service:nth-child(3n){border-right:none}
.service:nth-child(n+4){border-bottom:none;padding-top:36px}
.service h4{font-family:"Montserrat",sans-serif;font-size:22px;font-weight:400;color:#222;margin-top:18px}
.service p{margin:12px auto 0;width:200px;font-size:12px;font-style:italic;line-height:17px;color:var(--grey)}
.service span{display:block;width:44px;height:3px;background:var(--grey-dark);margin:26px auto 0}
.skyline{left:0;top:2509px;width:1200px;height:246px;background:linear-gradient(180deg,#ffffff 0%,#f1f1f1 40%,#dcdcdc 100%)}

/* projects */
.projects{left:0;top:2755px;width:1200px;height:747px;background:var(--night)}
.projects-title{left:172px;top:2848px;font-family:"Montserrat",sans-serif;font-size:42px;font-weight:300;color:var(--white)}
.filters{left:180px;top:2934px;display:flex;gap:28px;font-family:"Montserrat",sans-serif;font-size:12px;font-weight:500;color:var(--grey-light);text-transform:uppercase}
.filters .active{color:var(--white);border-bottom:2px solid var(--red);padding-bottom:6px}
.tile{top:3023px;height:355px}
.tile-featured{border:8px solid var(--red);background:linear-gradient(160deg,#3a3a3a,#1e1e1e)}
.tile-featured .overlay{position:absolute;inset:0;background:rgba(20,20,20,.55);display:flex;flex-direction:column;align-items:center;justify-content:center;gap:22px}
.tile-featured h5{font-family:"Montserrat",sans-serif;font-size:20px;font-weight:500;color:var(--white);text-transform:uppercase}
.all-projects{left:177px;top:3423px;font-family:"Montserrat",sans-serif;font-size:12px;font-weight:600;color:var(--white);border-bottom:2px solid var(--red);padding-bottom:5px}
.gallery-nav{left:948px;top:3420px;display:flex;gap:18px}

/* testimonials */
.testimonials{left:0;top:3502px;width:1200px;height:341px;background:linear-gradient(100deg,#4a4a4a 0%,#3b3b3b 45%,#2b2b2b 70%,#545045 100%)}
.testi-title{left:203px;top:3532px;font-family:"Montserrat",sans-serif;font-size:44px;font-weight:300;color:var(--white)}
.testi-text{left:203px;top:3617px;width:420px;font-size:13px;line-height:19px;color:#e6e6e6}
.avatar{left:203px;top:3700px;width:56px;height:56px;border-radius:50%;background:#9db2c8;border:3px solid var(--white)}
.testi-name{left:290px;top:3712px;font-family:"Montserrat",sans-serif;font-size:14px;font-weight:600;color:var(--red)}
.testi-role{left:290px;top:3733px;font-size:12px;color:var(--grey-light)}

/* partners */
.partners-title{left:174px;top:3955px;width:420px;font-family:"Montserrat",sans-serif;font-size:42px;font-weight:400;line-height:50px;color:#222}
.partners-text{left:174px;width:400px;font-size:12.5px;line-height:18px;color:var(--grey)}
.all-partners{left:174px;top:4246px;font-family:"Montserrat",sans-serif;font-size:12px;font-weight:600;color:#222;border-bottom:2px solid var(--red);padding-bottom:5px}
.badge{background:#cfcfcf}

/* call to action */
.cta{left:0;top:4355px;width:1200px;height:131px;background:var(--red)}
.cta-text{left:120px;top:4378px;width:580px;font-family:"Montserrat",sans-serif;font-size:25px;font-weight:400;line-height:32px;color:var(--white);text-transform:uppercase;text-align:center}
.cta-text strong{font-weight:700}
.cta-action{left:790px;top:4400px;display:flex;align-items:center;gap:14px;font-family:"Montserrat",sans-serif;font-size:15px;font-weight:600;color:var(--white);text-transform:uppercase;line-height:20px}

/* footer */
.footer{left:0;top:4486px;width:1200px;height:400px;background:linear-gradient(180deg,#1d1d1d,#121212)}
.footer h6{font-family:"Montserrat",sans-serif;font-size:17px;font-weight:500;color:var(--white)}
.footer-col{top:4528px}
.footer-col p,.footer-col li{font-size:11.5px;line-height:17px;color:var(--grey-light);list-style:none}
.field{width:250px;height:30px;background:#2a2a2a;border:1px solid #3a3a3a;margin-top:8px;font-size:11px;color:var(--grey);padding:7px 10px}
.btn-red{background:var(--red);color:var(--white);font-family:"Montserrat",sans-serif;font-size:11px;font-weight:600;text-transform:uppercase;display:flex;align-items:center;justify-content:center}
.pay{height:28px;background:var(--white);border-radius:3px;font-family:"Open Sans",sans-serif;font-size:10px;font-weight:700;color:var(--grey-dark);display:flex;align-items:center;justify-content:center}
.foot-social{display:flex;gap:6px;margin-top:22px}
.foot-social span{width:24px;height:24px;background:#2c2c2c;display:flex;align-items:center;justify-content:center}
.foot-social span i{width:8px;height:8px;border-radius:50%;background:var(--grey-light);display:block}
.to-top{left:580px;top:4838px;width:40px;height:28px;background:var(--red);display:flex;align-items:center;justify-content:center}
.copyright{left:0;top:4872px;width:1200px;text-align:center;font-size:10px;line-height:14px;color:var(--grey)}
.copyright a{color:var(--red);text-decoration:none}
.live-chat{left:846px;top:4892px;width:164px;height:26px;background:var(--chat);color:var(--white);font-family:"Montserrat",sans-serif;font-size:12px;font-weight:600;display:flex;align-items:center;justify-content:center;gap:8px}
</style>
</head>
<body>

<!-- header -->
<header class="abs site-header">
  <div class="abs brand" style="position:absolute">
    <span class="brand-mark"></span>
    <span class="brand-name">Brindlecrest Roofing</span>
  </div>
  <nav class="abs main-nav">
    <a href="#">HOME</a><a href="#">ABOUT US</a><a href="#">SERVICES</a><a href="#">PROJECTS</a><a href="#">CONTACT US</a>
  </nav>
  <div class="abs header-phone">
    <svg width="22" height="22" viewBox="0 0 24 24" fill="none" stroke="#fff" stroke-width="1.8"><path d="M5 3h4l2 5-3 2a12 12 0 0 0 6 6l2-3 5 2v4a2 2 0 0 1-2 2A17 17 0 0 1 3 5a2 2 0 0 1 2-2z"/></svg>
    555-014-2200
  </div>
  <div class="abs search-btn">
    <svg width="26" height="26" viewBox="0 0 24 24" fill="none" stroke="#fff" stroke-width="2"><circle cx="10" cy="10" r="7"/><path d="M15 15l6 6"/></svg>
  </div>
</header>

<!-- hero -->
<section>
  <div class="abs hero" role="img" aria-label="Photo of a roofer working on a house roof at dusk"></div>
  <div class="abs hero-shade"></div>
  <h1 class="abs hero-title">When it comes to your<br>home, think <strong>Brindlecrest!</strong></h1>
  <div class="abs slide-arrow" style="left:52px"><svg width="14" height="14" viewBox="0 0 14 14"><path d="M9 2L4 7l5 5" fill="none" stroke="#fff" stroke-width="2"/></svg></div>
  <div class="abs slide-arrow" style="left:1082px"><svg width="14" height="14" viewBox="0 0 14 14"><path d="M5 2l5 5-5 5" fill="none" stroke="#fff" stroke-width="2"/></svg></div>
  <div class="abs social-rail">
    <span aria-label="Linkora"><i></i></span><span aria-label="Chirpline"><i></i></span><span aria-label="Workhive"><i></i></span><span aria-label="Circlenet"><i></i></span><span aria-label="Pinwall"><i></i></span><span aria-label="Settings"><i></i></span>
  </div>
  <div class="abs quote-card">
    <p>Looking for a quality and affordable constructor for your next project?</p>
    <a href="#">REQUEST A QUOTE</a>
  </div>
</section>

<!-- stats -->
<section class="abs stats"></section>
<div class="abs stat-number">2250</div>
<div class="abs stat-title">Completed Projects</div>
<p class="abs stat-sub">We have built our success by providing homeowners as well as small businesses in the entire Chicagoland and Greater Indiana</p>

<!-- about -->
<section>
  <div class="abs about-photo" role="img" aria-label="Roofer in hard hat and tool belt holding a hammer"></div>
  <h2 class="abs about-title">We are a family owned, owner operated company as well as a Full-Time Professional Roofing Company</h2>
  <ul class="abs about-list">
    <li>We are proud to say We Are Family Owned and Operated and have over 30 years of experience</li>
    <li>We are fully Licensed, Bonded &amp; Insured</li>
    <li>We only use the best quality materials that Meet or Exceed all Industry Standards</li>
    <li>We are a Second Generation Roofing company</li>
    <li>All Warranties will be given in writing to ensure you chose a company you can rely on</li>
    <li>We will give every job the quality, time and craftsmanship as if it were our very own home</li>
  </ul>
  <a class="abs read-more" href="#">READ MORE</a>
</section>

<!-- features -->
<section>
  <div class="abs feature" style="left:0;background:var(--grey-dark)">
    <svg width="70" height="70" viewBox="0 0 70 70" fill="none" stroke="#ec1f27" stroke-width="3"><circle cx="35" cy="28" r="18"/><circle cx="35" cy="28" r="10"/><path d="M24 42l-6 20 9-4 6 8 2-10M46 42l6 20-9-4-6 8-2-10"/></svg>
    <h3>Quality work at competitive rates</h3>
    <p>Every roof we finish is built to last, priced fairly and backed by honest, careful work from start to end.</p>
  </div>
  <div class="abs feature" style="left:400px;background:var(--red)">
    <svg width="70" height="70" viewBox="0 0 70 70" fill="none" stroke="#fff" stroke-width="3"><path d="M8 36L36 8h26v26L34 62z"/><circle cx="50" cy="20" r="4"/><path d="M26 44l16-16"/><circle cx="28" cy="32" r="3"/><circle cx="40" cy="42" r="3"/></svg>
    <h3>Senior Discounts / Free Estimates</h3>
    <p>Our estimates are always free, and seniors receive a special discount on all of our roofing work.</p>
  </div>
  <div class="abs feature" style="left:800px;background:var(--grey)">
    <svg width="70" height="70" viewBox="0 0 70 70" fill="none" stroke="#ec1f27" stroke-width="3"><circle cx="35" cy="35" r="27"/><path d="M35 18v18l11 8"/></svg>
    <h3>7 Day Service / Right People and Tools</h3>
    <p>Our crews work seven days a week with the right people and the right tools for every job.</p>
  </div>
</section>

<!-- services -->
<section>
  <h2 class="abs section-title" style="top:1775px;font-size:36px">Our Services</h2>
  <p class="abs services-intro">From small repairs to full replacements, our crews handle every roof with care, skill and clear pricing so you always know what to expect from us.</p>
  <div class="abs services-grid">
    <div class="service">
      <svg width="60" height="54" viewBox="0 0 60 54" fill="none" stroke="#ec1f27" stroke-width="2.5"><path d="M4 28L30 6l26 22M10 23v27h40V23"/><rect x="24" y="32" width="12" height="18"/></svg>
      <h4>Single Roofs</h4><p>Durable shingle roofs installed with care and backed by a strong warranty.</p><span></span>
    </div>
    <div class="service">
      <svg width="60" height="54" viewBox="0 0 60 54" fill="none" stroke="#ec1f27" stroke-width="2.5"><path d="M6 24L30 4l24 20M12 20v30h36V20M20 30h20v20H20z"/></svg>
      <h4>Flat Roofs</h4><p>Sealed flat roof systems for homes and commercial buildings of any size.</p><span></span>
    </div>
    <div class="service">
      <svg width="60" height="54" viewBox="0 0 60 54" fill="none" stroke="#ec1f27" stroke-width="2.5"><path d="M4 26L30 4l26 22M10 21v29h40V21"/><path d="M26 26l8 8-6 4 6 10"/></svg>
      <h4>Storm Damage</h4><p>Fast repairs after wind, hail or storms to keep your home safe and dry.</p><span></span>
    </div>
    <div class="service">
      <svg width="60" height="54" viewBox="0 0 60 54" fill="none" stroke="#ec1f27" stroke-width="2.5"><rect x="12" y="6" width="36" height="40"/><path d="M30 6v40M12 26h36M8 50h44"/></svg>
      <h4>Windows</h4><p>New window fitting that saves energy and brightens every room inside.</p><span></span>
    </div>
    <div class="service">
      <svg width="60" height="54" viewBox="0 0 60 54" fill="none" stroke="#ec1f27" stroke-width="2.5"><path d="M14 10h26v14H14zM40 14h10v6H40M22 24l-4 24h10l2-24"/></svg>
      <h4>Carpentry</h4><p>Skilled woodwork for decks, frames, trims and custom home projects.</p><span></span>
    </div>
    <div class="service">
      <svg width="60" height="54" viewBox="0 0 60 54" fill="none" stroke="#ec1f27" stroke-width="2.5"><path d="M16 6h28l6 12H10zM8 18h44v6H8zM12 24v24h36V24M22 30v12M30 30v12M38 30v12"/></svg>
      <h4>Kitchens &amp; Baths</h4><p>Fresh kitchen and bath remodels built to your taste and your budget.</p><span></span>
    </div>
  </div>
  <div class="abs skyline" role="img" aria-label="Light line drawing of a city skyline"></div>
</section>

<!-- projects -->
<section>
  <div class="abs projects"></div>
  <h2 class="abs projects-title">Our Recent Projects</h2>
  <div class="abs filters"><span class="active">All</span><span>Buildings</span><span>Family House</span><span>Interior</span><span>Office</span></div>
  <div class="abs tile tile-featured" style="left:0;width:354px" role="img" aria-label="Modern dark business center building">
    <div class="overlay">
      <svg width="34" height="22" viewBox="0 0 34 22" fill="none" stroke="#fff" stroke-width="2"><path d="M1 11C6 3 12 1 17 1s11 2 16 10c-5 8-11 10-16 10S6 19 1 11z"/><circle cx="17" cy="11" r="4"/></svg>
      <h5>Business Center</h5>
      <svg width="28" height="28" viewBox="0 0 28 28" fill="none" stroke="#fff" stroke-width="2.5"><path d="M12 16l4-4M10 12l-4 4a4 4 0 0 0 6 6l4-4M18 16l4-4a4 4 0 0 0-6-6l-4 4"/></svg>
    </div>
  </div>
  <div class="abs tile" style="left:354px;width:374px;background:linear-gradient(160deg,#cfd3d6 0%,#8a7a66 50%,#4c4c4c 100%)" role="img" aria-label="Modern house with wood panel facade"></div>
  <div class="abs tile" style="left:728px;width:371px;background:linear-gradient(170deg,#d9dde2 0%,#9a958d 45%,#6e6a62 75%,#7b8f5a 100%)" role="img" aria-label="Row of modern family houses"></div>
  <div class="abs tile" style="left:1099px;width:101px;background:linear-gradient(170deg,#d4d8dc,#8d8a80)" role="img" aria-label="Modern townhouse"></div>
  <div class="abs all-projects">ALL PROJECTS</div>
  <div class="abs gallery-nav">
    <svg width="14" height="14" viewBox="0 0 14 14"><path d="M9 2L4 7l5 5" fill="none" stroke="#fff" stroke-width="2"/></svg>
    <svg width="14" height="14" viewBox="0 0 14 14"><path d="M5 2l5 5-5 5" fill="none" stroke="#fff" stroke-width="2"/></svg>
  </div>
</section>

<!-- testimonials -->
<section>
  <div class="abs testimonials" role="img" aria-label="Background photo of a roofer in a hard hat"></div>
  <h2 class="abs testi-title">Testimonials</h2>
  <p class="abs testi-text">The crew arrived on time, kept the yard clean and finished our new roof in two days. Great price, clear answers and friendly people from start to finish.</p>
  <div class="abs avatar" role="img" aria-label="Customer portrait"></div>
  <div class="abs testi-name">Dana Morrow</div>
  <div class="abs testi-role">Client</div>
</section>

<!-- partners -->
<section>
  <h2 class="abs partners-title">We Work With The Best Partners</h2>
  <p class="abs partners-text" style="top:4068px">We team up with trusted suppliers and trade groups so every job uses proven materials, fair pricing and support you can count on for years.</p>
  <p class="abs partners-text" style="top:4150px">Our partners share our focus on safety, quality and service, which helps us deliver strong results on homes and commercial buildings alike.</p>
  <div class="abs all-partners">ALL PARTNERS</div>
  <div class="abs badge" style="left:612px;top:3928px;width:190px;height:100px;clip-path:polygon(0 60%,50% 0,100% 60%,100% 100%,0 100%)"></div>
  <div class="abs badge" style="left:860px;top:3918px;width:118px;height:118px"></div>
  <div class="abs badge" style="left:630px;top:4120px;width:160px;height:70px;border-radius:6px"></div>
  <div class="abs badge" style="left:845px;top:4110px;width:170px;height:80px;border-radius:40px"></div>
</section>

<!-- call to action -->
<section>
  <div class="abs cta"></div>
  <svg class="abs" style="left:720px;top:4355px" width="480" height="131" viewBox="0 0 480 131"><path d="M0 0h480v131H0l40-65.5z" fill="#c4151c"/></svg>
  <p class="abs cta-text">Looking for a quality and affordable constructor for your <strong>next project?</strong></p>
  <div class="abs cta-action">
    <svg width="34" height="34" viewBox="0 0 34 34" fill="none" stroke="#fff" stroke-width="2"><rect x="5" y="3" width="20" height="26"/><path d="M10 10h10M10 16h10M10 22h6M22 24l8-8 2 2-8 8h-2z"/></svg>
    <span>Request a quote</span>
  </div>
</section>

<!-- footer -->
<footer>
  <div class="abs footer"></div>
  <div class="abs footer-col" style="left:174px;width:260px">
    <h6>Contact Us</h6>
    <p style="margin-top:24px">Brindlecrest Roofing &amp; Construction<br>Company, Inc.</p>
    <p style="margin-top:10px">Roofing License: &nbsp; # 104-0201<br>&nbsp; &nbsp; &nbsp; &nbsp; &nbsp; &nbsp; &nbsp; &nbsp; &nbsp; &nbsp; &nbsp; &nbsp; &nbsp; &nbsp; &nbsp; # 105-0377</p>
    <p style="margin-top:18px">555-014-2200 (Illinois)<br>555-014-3377 (Indiana)</p>
    <div class="foot-social"><span aria-label="Linkora"><i></i></span><span aria-label="Chirpline"><i></i></span><span aria-label="Workhive"><i></i></span><span aria-label="Circlenet"><i></i></span><span aria-label="Pinwall"><i></i></span></div>
  </div>
  <div class="abs footer-col" style="left:469px;width:260px">
    <h6>Quick Contact</h6>
    <div style="margin-top:16px">
      <div class="field">Name</div>
      <div class="field">Email</div>
      <div class="field" style="height:70px">Message</div>
    </div>
    <div class="btn-red" style="position:absolute;left:168px;top:208px;width:82px;height:28px">Submit</div>
  </div>
  <div class="abs footer-col" style="left:760px;width:270px">
    <h6>Newsletter</h6>
    <div style="display:flex;margin-top:24px">
      <div class="field" style="width:170px;margin-top:0">Email</div>
      <div class="btn-red" style="width:92px;height:30px">Subscribe</div>
    </div>
    <p style="margin-top:10px">Subscribe to our newsletter for latest updates</p>
    <div style="display:flex;gap:6px;margin-top:26px">
      <span class="pay" style="width:58px">coinwell</span>
      <span class="pay" style="width:58px">Cardora</span>
      <span class="pay" style="width:52px">Vantix</span>
      <span class="pay" style="width:62px">Amerline</span>
    </div>
  </div>
  <div class="abs to-top"><svg width="14" height="10" viewBox="0 0 14 10"><path d="M2 8l5-5 5 5" fill="none" stroke="#fff" stroke-width="2"/></svg></div>
  <p class="abs copyright">© Copyright Brindlecrest Roofing<br>Designed by <a href="#">MakerHarbor</a></p>
  <div class="abs live-chat">
    <svg width="14" height="12" viewBox="0 0 14 12" fill="#fff"><path d="M1 1h12v8H5l-3 3V9H1z"/></svg>
    Live Chat
  </div>
</footer>

</body>
</html>
```